Brightstone Roofing Business Card

This is my current business card. But I’d like to make some changes. Somewhere on the card I’d like to list some of the services we offer. Maybe on the back? But I’d still like to keep the red. White and black modern look.

-residential & commercial roofing
-Roof Repairs & Maintenance
-Storm Damage & Insurance Claims specialist
-Christmas Lights and permanent Christmas lights
Fencing. Windows. Gutters. Siding. Sheetrock, painting.

```html
<!DOCTYPE html>
<html lang="en">
<head>
<meta charset="utf-8">
<title>Brightstone Roofing Co. – Business Card</title>
<link href="https://fonts.googleapis.com/css2?family=Lato:wght@400;700;900&display=swap" rel="stylesheet">
<style>
  :root {
    --bg: #1f1e1e;
    --card-dark: #232324;
    --card-light: #ffffff;
    --red: #e3161b;
    --red-deep: #b3121a;
    --ink: #161616;
    --grey: #8e8e90;
    --soft: #c9c9cb;
    --rule: #3a3a3c;
    --text: #3a3a3a;
  }
  * { margin: 0; padding: 0; box-sizing: border-box; }
  html, body { width: 1200px; height: 939px; overflow: hidden; background: var(--bg); }
  body { position: relative; font-family: "Lato", sans-serif; }

  .card {
    position: absolute;
    left: 290px;
    width: 620px;
    height: 354px;
    border-radius: 18px;
    overflow: hidden;
  }

  /* Back */
  .card-back { top: 80px; background: var(--card-dark); }
  .card-back .emblem {
    position: absolute; left: 250px; top: 30px;
    width: 120px; height: 120px; border-radius: 50%;
    background: radial-gradient(circle at 40% 40%, var(--red), var(--red-deep));
  }
  .card-back .wordmark {
    position: absolute; left: 0; right: 0; top: 166px;
    text-align: center; font-weight: 900; letter-spacing: 2px;
  }
  .card-back .wordmark-main { display: block; font-size: 38px; color: var(--red); line-height: 1; }
  .card-back .wordmark-sub { display: block; font-size: 20px; color: var(--grey); margin-top: 6px; line-height: 1; }

  .services {
    position: absolute; left: 40px; right: 40px; top: 250px;
    border-top: 1px solid var(--rule);
    padding-top: 12px;
    list-style: none;
    text-align: center;
    font-size: 12.5px; line-height: 1.7; color: var(--soft);
  }
  .services li { display: block; }
  .services .dot { color: var(--red); font-weight: 900; padding: 0 6px; }

  /* Front */
  .card-front { top: 505px; background: var(--card-light); }
  .card-front .edge-mark {
    position: absolute; left: 0; top: 178px; width: 10px; height: 42px; background: var(--ink);
  }
  .card-front .wordmark {
    position: absolute; left: 42px; top: 42px; font-weight: 900; letter-spacing: 1px;
  }
  .card-front .wordmark-main { display: block; font-size: 32px; color: var(--red); line-height: 1; }
  .card-front .wordmark-sub { display: block; font-size: 20px; color: var(--ink); margin-top: 6px; line-height: 1; }

  .person { position: absolute; left: 42px; top: 140px; }
  .person-name { font-size: 30px; font-weight: 700; color: var(--red); line-height: 1; letter-spacing: 0.5px; }
  .person-role { font-size: 15px; color: var(--ink); margin-top: 6px; }

  .contact { position: absolute; left: 42px; top: 222px; list-style: none; }
  .contact li { display: flex; align-items: flex-start; gap: 10px; font-size: 14px; color: var(--text); line-height: 1.35; margin-bottom: 6px; }
  .contact svg { flex: none; width: 13px; height: 13px; margin-top: 3px; fill: var(--red); }

  .hero-mark {
    position: absolute; left: 330px; top: 48px;
    width: 260px; height: 260px; border-radius: 50%;
    background: radial-gradient(circle at 38% 35%, var(--red) 0%, var(--red-deep) 100%);
  }
</style>
</head>
<body>

  <section class="card card-back" aria-label="Card back">
    <div class="emblem" role="img" aria-label="Brand emblem area"></div>
    <div class="wordmark">
      <span class="wordmark-main">BRIGHTSTONE</span>
      <span class="wordmark-sub">ROOFING CO.</span>
    </div>
    <ul class="services" aria-label="Services">
      <li>Residential &amp; Commercial Roofing<span class="dot">•</span>Roof Repairs &amp; Maintenance</li>
      <li>Storm Damage &amp; Insurance Claims Specialist<span class="dot">•</span>Christmas &amp; Permanent Christmas Lights</li>
      <li>Fencing<span class="dot">•</span>Windows<span class="dot">•</span>Gutters<span class="dot">•</span>Siding<span class="dot">•</span>Sheetrock<span class="dot">•</span>Painting</li>
    </ul>
  </section>

  <section class="card card-front" aria-label="Card front">
    <div class="edge-mark"></div>
    <div class="wordmark">
      <span class="wordmark-main">BRIGHTSTONE</span>
      <span class="wordmark-sub">ROOFING CO.</span>
    </div>

    <div class="person">
      <p class="person-name">DANA WHITFIELD</p>
      <p class="person-role">Owner</p>
    </div>

    <ul class="contact">
      <li>
        <svg viewBox="0 0 24 24"><path d="M12 2a7 7 0 0 0-7 7c0 5 7 13 7 13s7-8 7-13a7 7 0 0 0-7-7zm0 9.5A2.5 2.5 0 1 1 12 6.5a2.5 2.5 0 0 1 0 5z"/></svg>
        <span>418 Orchard Ln Millbrook<br>TX 75000, United States</span>
      </li>
      <li>
        <svg viewBox="0 0 24 24"><path d="M6.6 10.8a15 15 0 0 0 6.6 6.6l2.2-2.2a1 1 0 0 1 1-.25 11.4 11.4 0 0 0 3.6.6 1 1 0 0 1 1 1V20a1 1 0 0 1-1 1A17 17 0 0 1 3 4a1 1 0 0 1 1-1h3.5a1 1 0 0 1 1 1c0 1.25.2 2.45.6 3.6a1 1 0 0 1-.25 1z"/></svg>
        <span>555-014-2286</span>
      </li>
      <li>
        <svg viewBox="0 0 24 24"><path d="M3 5h18v14H3zm2 2v.5l7 4.5 7-4.5V7l-7 4.5z"/></svg>
        <span>dana@brightstoneroofing.co</span>
      </li>
      <li>
        <svg viewBox="0 0 24 24"><path d="M12 2a10 10 0 1 0 0 20 10 10 0 0 0 0-20zm0 2a8 8 0 0 1 7.7 6H4.3A8 8 0 0 1 12 4zm0 16a8 8 0 0 1-7.7-6h15.4A8 8 0 0 1 12 20z"/></svg>
        <span>brightstoneroofing.co</span>
      </li>
    </ul>

    <div class="hero-mark" role="img" aria-label="Large brand emblem area"></div>
  </section>

</body>
</html>
```